New Design for Poker Card Box

Looking for someone to design a Poker Card Box for my newly design Poker Cards. The box has to new and modem, I'm open to suggestions, the end product should be unique and amazing enough that people would want to buy this deck of cards.
The gold trim on the sample box attached will be printed in gold foil and must be produced as a separate layer for easier printing. THIS IS ESSENTIAL.
- My logo on the box is essential
- The writing on the bottom flap 'Copyright 2021 Crimson Lantern Studios, Sydney, Australia, Printed by RWTB'. should also be there.
- The words Playing Cards and Premium Edition should also be there.
- My website is www.crimsonlantern.com.au you can also use the banner from my home page if need be.
- I like the Vegas header I have with the Ferrow Span and Lyric Dome in the background, if I can get a few designs with these visible that would be good.
- I tried to attach the images of the face of the cards but the file is 8.8MB and wouldn't load. I can maybe get these to you somehow if need be.

Please feel free to message if I've missed anything or if you have any questions.

Gus

Target Market(s)

Poker enthusiasts, Poker Card collectors, mainly US market

Requirements
Must have
• All must haves are noted in the Project Description.

```html
<!DOCTYPE html>
<html lang="en">
<head>
<meta charset="utf-8">
<title>Crimson Lantern Studios – Playing Cards Box Dieline</title>
<link rel="stylesheet" href="https://fonts.googleapis.com/css2?family=Oswald:wght@400;600&family=Yellowtail&family=Roboto:wght@500&display=swap">
<style>
  :root {
    --backdrop: #f1f1f1;
    --panel-black: #1d1b1d;
    --chip-amber: #f6b21b;
    --script-gold: #e3c46a;
    --edition-gold: #d9c07a;
    --cut-magenta: #d1388f;
    --copy-white: #ffffff;
  }
  html, body {
    margin: 0;
    width: 1200px;
    height: 716px;
    overflow: hidden;
    background: radial-gradient(ellipse at 60% 45%, #fafafa 0%, var(--backdrop) 60%, #e4e4e4 100%);
  }
  .dieline { display: block; width: 1200px; height: 716px; }
  .foil { fill: url(#goldFoil); }
  .panel-black { fill: var(--panel-black); }
  .cut-line { fill: none; stroke: var(--cut-magenta); stroke-width: 0.8; }
  .fold-line { fill: none; stroke: var(--cut-magenta); stroke-width: 0.5; stroke-dasharray: 2 2; }
  .gold-frame { fill: none; stroke: url(#goldFoil); stroke-width: 2.2; }
  .chip-dot { fill: var(--chip-amber); }
  .brand-name {
    font-family: "Oswald", sans-serif; font-weight: 600;
    fill: var(--chip-amber); text-anchor: middle; letter-spacing: 0.5px;
  }
  .spine-name {
    font-family: "Oswald", sans-serif; font-weight: 600;
    fill: url(#goldFoil); text-anchor: middle; letter-spacing: 2px;
  }
  .title-script {
    font-family: "Yellowtail", cursive; fill: var(--script-gold); text-anchor: middle;
  }
  .edition {
    font-family: "Oswald", sans-serif; font-weight: 400;
    fill: var(--edition-gold); text-anchor: middle;
  }
  .copyright {
    font-family: "Roboto", sans-serif; font-weight: 500;
    fill: var(--copy-white); text-anchor: middle;
  }
  .city-photo { fill: url(#cityNight); }
  .thumb-notch { fill: var(--backdrop); }
  .glue-flap { fill: url(#glueFade); }
</style>
</head>
<body>
<svg class="dieline" viewBox="0 0 1200 716" xmlns="http://www.w3.org/2000/svg">
  <defs>
    <linearGradient id="goldFoil" x1="0" y1="0" x2="1" y2="1">
      <stop offset="0" stop-color="#a9822a"/>
      <stop offset="0.25" stop-color="#f6df8c"/>
      <stop offset="0.5" stop-color="#c49a3a"/>
      <stop offset="0.75" stop-color="#f3d77a"/>
      <stop offset="1" stop-color="#9c7524"/>
    </linearGradient>
    <linearGradient id="cityNight" x1="0" y1="0" x2="0" y2="1">
      <stop offset="0" stop-color="#0b0a10"/>
      <stop offset="0.35" stop-color="#5a4320"/>
      <stop offset="0.6" stop-color="#c89a4a"/>
      <stop offset="0.85" stop-color="#1f3a5e"/>
      <stop offset="1" stop-color="#0a0c18"/>
    </linearGradient>
    <linearGradient id="glueFade" x1="0" y1="0" x2="0" y2="1">
      <stop offset="0" stop-color="#e9c96a"/>
      <stop offset="0.3" stop-color="#8a6a28"/>
      <stop offset="0.5" stop-color="#1d1b1d"/>
      <stop offset="1" stop-color="#1d1b1d"/>
    </linearGradient>

    <g id="faceArtwork">
      <rect class="foil" x="0" y="130" width="232" height="310"/>
      <rect class="panel-black" x="6" y="136" width="220" height="298" rx="6"/>
      <rect class="gold-frame" x="6" y="136" width="220" height="298" rx="6"/>
      <circle class="chip-dot" cx="116" cy="176" r="12"/>
      <text class="brand-name" x="116" y="210" font-size="17">CRIMSON LANTERN</text>
      <text class="brand-name" x="116" y="226" font-size="11">STUDIOS</text>
      <text class="title-script" x="116" y="294" font-size="30">Playing Cards</text>
      <text class="edition" x="116" y="318" font-size="11">Premium Edition</text>
      <rect class="city-photo" x="7" y="326" width="218" height="107" rx="4"
            role="img" aria-label="Night-time aerial photograph of the city skyline with lit casinos, Ferrow Span and Lyric Dome, and a glowing fountain"/>
      <rect class="gold-frame" x="6" y="136" width="220" height="298" rx="6"/>
      <rect class="panel-black" x="0" y="440" width="232" height="65"/>
    </g>

    <g id="spineArtwork">
      <rect class="foil" x="0" y="130" width="60" height="310"/>
      <rect class="panel-black" x="5" y="134" width="50" height="302" rx="4"/>
      <text class="spine-name" transform="translate(30 285) rotate(90)" y="11" font-size="30" textLength="270" lengthAdjust="spacingAndGlyphs">CRIMSON LANTERN</text>
    </g>
  </defs>

  <g class="box-net" transform="translate(171 26) scale(1.3)">
    <!-- left spine with dust flaps -->
    <path class="foil" d="M5,130 L5,82 L14,66 L56,66 L65,78 L65,130 Z"/>
    <use href="#spineArtwork" x="5"/>
    <path class="panel-black" d="M5,440 L65,440 L65,468 L56,490 L14,490 L5,468 Z"/>

    <!-- front panel with tuck lid -->
    <path class="foil" d="M65,130 L65,48 Q65,2 182,2 Q300,2 300,48 L300,130 Z"/>
    <line class="fold-line" x1="65" y1="55" x2="300" y2="55"/>
    <g class="front-face"><use href="#faceArtwork" x="67"/></g>

    <!-- right spine with dust flaps -->
    <path class="foil" d="M300,130 L300,78 L309,66 L356,66 L365,82 L365,130 Z"/>
    <use href="#spineArtwork" x="303"/>
    <path class="panel-black" d="M303,440 L363,440 L363,468 L354,490 L312,490 L303,468 Z"/>

    <!-- back panel -->
    <g class="back-face">
      <use href="#faceArtwork" x="365"/>
      <path class="thumb-notch" d="M463,130 A18,18 0 0 0 499,130 Z"/>
      <text class="copyright" x="481" y="464" font-size="6.6">Copyright 2021 Crimson Lantern Studios,</text>
      <text class="copyright" x="481" y="474" font-size="6.6">Sydney, Australia, Printed by RWTB</text>
      <text class="copyright" x="481" y="492" font-size="9" letter-spacing="3">♠♥♦♣</text>
    </g>

    <!-- glue flap -->
    <path class="glue-flap" d="M597,130 L650,140 L660,150 L660,478 L650,492 L597,505 Z"/>

    <!-- fold lines -->
    <line class="fold-line" x1="65" y1="130" x2="597" y2="130"/>
    <line class="fold-line" x1="5" y1="440" x2="597" y2="440"/>

    <!-- outer cut line -->
    <path class="cut-line" d="M5,82 L14,66 L56,66 L65,78 L65,48 Q65,2 182,2 Q300,2 300,48 L300,78 L309,66 L356,66 L365,82 L365,130 L463,130 A18,18 0 0 0 499,130 L597,130 L650,140 L660,150 L660,478 L650,492 L597,505 L365,505 L365,440 L363,440 L363,468 L354,490 L312,490 L303,468 L303,440 L300,440 L300,505 L67,505 L67,440 L65,440 L65,468 L56,490 L14,490 L5,468 Z"/>
  </g>
</svg>
</body>
</html>
```